PLUMBER,DRAINER,GASFITTER/LPG
blocked drains
new installations
maintenance
stormwater
gutters
all plumbing requirements
no job to small
HONEST RELIABLE FAIR
HI I'm after a professional flyer something that grabs the eye with all the above information in point form, i want to offer free quotes aswell.!
i want my email on there .... tradesbelvine.com
also i want have ...... 24 hour emergency service on there in red and
my lic no 482091k.
and I'm on Facebook under MOSSGATE PLUMBING aswell.
any other information needed its on my website as above
i like the colours black and blue as in photo uploaded .
but very open to anything that you think could be good,

```html
<!DOCTYPE html>
<html lang="en">
<head>
<meta charset="utf-8">
<title>Mossgate Plumbing Flyer</title>
<link rel="stylesheet" href="https://fonts.googleapis.com/css2?family=Montserrat:wght@600;700&family=Signika:wght@400;600&display=swap">
<style>
  :root {
    --navy: #262262;
    --cyan: #1ca8e0;
    --pink: #e6248d;
    --red: #e0262b;
    --paper: #f5f5f7;
    --backdrop: #e8edf1;
    --white: #ffffff;
    --ink: #1d1d1d;
  }
  * { margin: 0; padding: 0; box-sizing: border-box; }
  html, body { width: 1200px; height: 1200px; overflow: hidden; background: var(--backdrop); }
  .flyer {
    position: absolute; left: 198px; top: 30px; width: 804px; height: 1140px;
    background: linear-gradient(180deg, var(--white), var(--paper));
    box-shadow: 0 6px 18px rgba(0,0,0,.18);
    overflow: hidden;
    font-family: "Signika", sans-serif;
    color: var(--navy);
  }
  .header-band { position: absolute; left: 0; top: 0; }
  .site-url {
    position: absolute; left: 56px; top: 42px;
    font-family: "Montserrat", sans-serif; font-weight: 600; font-size: 17px; color: var(--white);
  }
  .photo-frame { position: absolute; }
  .photo-fill { position: absolute; border-radius: 10px; }
  .frame-hero { left: 289px; top: 44px; width: 450px; height: 316px; background: var(--navy); border-radius: 20px 20px 34px 20px; }
  .frame-hero .photo-fill { inset: 14px 20px 4px 4px; background: linear-gradient(135deg, #e7e9ee 0%, #5b78b8 45%, #3d5596 70%, #d9dce3 100%); }
  .frame-fitting { left: 82px; top: 128px; width: 198px; height: 232px; background: var(--cyan); border-radius: 12px 20px 12px 28px; }
  .frame-fitting .photo-fill { inset: 12px 4px 4px 12px; background: linear-gradient(150deg, #c9ccd1 0%, #b8904a 45%, #c7773f 65%, #f4f4f4 100%); }
  .frame-sink { left: 85px; top: 375px; width: 192px; height: 135px; background: var(--pink); border-radius: 10px 10px 14px 16px; }
  .frame-sink .photo-fill { inset: 4px 4px 10px 10px; background: linear-gradient(120deg, #e6e8ec 0%, #2e2e36 35%, #3c86cf 70%, #e6e8ec 100%); }
  .frame-basin { left: 289px; top: 369px; width: 278px; height: 195px; background: var(--navy); border-radius: 10px 20px 6px 18px; }
  .frame-basin .photo-fill { inset: 4px 16px 10px 4px; background: linear-gradient(135deg, #f1f2f4 0%, #e1e4e8 45%, #3f7fd0 75%, #eceef1 100%); }

  .emergency { position: absolute; left: 620px; top: 405px; width: 130px; color: var(--red); }
  .emergency svg { display: block; margin-left: 4px; }
  .emergency-hour { font-family: "Montserrat", sans-serif; font-weight: 700; font-size: 38px; line-height: 1; margin-top: 2px; }
  .emergency-note { font-family: "Montserrat", sans-serif; font-weight: 600; font-size: 16px; line-height: 1.3; }

  .trade-title {
    position: absolute; left: 88px; top: 550px;
    font-family: "Montserrat", sans-serif; font-weight: 700; font-size: 35px; line-height: 42px;
    color: var(--navy); letter-spacing: .3px;
  }
  .title-rule { position: absolute; left: 83px; top: 644px; width: 654px; height: 2px; background: var(--red); }

  .services-heading {
    position: absolute; left: 83px; top: 665px;
    font-weight: 600; font-size: 40px; letter-spacing: .5px;
    text-transform: uppercase; color: var(--navy);
  }
  .service-list { position: absolute; left: 91px; top: 717px; list-style: none; }
  .service-list li {
    position: relative; padding-left: 18px; height: 40px;
    font-weight: 600; font-size: 32px; line-height: 40px; color: var(--cyan);
  }
  .service-list li::before {
    content: ""; position: absolute; left: 0; top: 13px;
    border-left: 8px solid var(--navy); border-top: 7px solid transparent; border-bottom: 7px solid transparent;
  }
  .service-extra { position: absolute; left: 89px; top: 924px; font-weight: 600; font-size: 24px; line-height: 30px; }
  .licence { position: absolute; left: 84px; top: 998px; font-size: 21px; letter-spacing: .5px; }

  .brand { position: absolute; left: 477px; top: 672px; width: 260px; text-align: center; color: var(--cyan); }
  .brand-dot { width: 54px; height: 54px; border-radius: 50%; background: var(--cyan); margin: 0 auto 12px; }
  .brand-name { font-family: "Montserrat", sans-serif; font-weight: 700; font-size: 34px; line-height: 1.05; letter-spacing: 1px; }
  .brand-values { margin-top: 12px; font-family: "Montserrat", sans-serif; font-weight: 600; font-size: 15px; letter-spacing: 1px; color: var(--navy); }
  .free-quotes { margin-top: 6px; font-family: "Montserrat", sans-serif; font-weight: 700; font-size: 20px; color: var(--red); }

  .call-box { position: absolute; left: 477px; top: 916px; width: 260px; text-align: center; font-family: "Montserrat", sans-serif; font-weight: 600; }
  .call-label { font-size: 22px; color: var(--ink); line-height: 27px; }
  .call-number { font-size: 31px; color: var(--red); line-height: 38px; }

  .footer-band {
    position: absolute; left: 0; top: 1032px; width: 100%; height: 108px;
    background: var(--navy); color: var(--white); text-align: center;
    font-size: 19px; letter-spacing: .8px; padding-top: 12px; line-height: 28px;
  }
  .footer-band svg { vertical-align: -3px; margin-right: 6px; }
  .footer-gap { display: inline-block; width: 22px; }
</style>
</head>
<body>
<main class="flyer">
  <svg class="header-band" width="804" height="80" viewBox="0 0 804 80" aria-hidden="true">
    <path d="M0 0H804V36H294L245 77H0Z" fill="var(--navy)"/>
  </svg>
  <div class="site-url">tradesbelvine.com</div>

  <div class="photo-frame frame-hero"><div class="photo-fill" role="img" aria-label="Smiling plumber tightening a pipe under a sink with a red wrench"></div></div>
  <div class="photo-frame frame-fitting"><div class="photo-fill" role="img" aria-label="Close-up of a wrench on a brass fitting and copper pipe"></div></div>
  <div class="photo-frame frame-sink"><div class="photo-fill" role="img" aria-label="Plumber in blue cap fixing a sink trap"></div></div>
  <div class="photo-frame frame-basin"><div class="photo-fill" role="img" aria-label="Plumber in overalls repairing pipes beneath a bathroom basin"></div></div>

  <div class="emergency">
    <svg width="84" height="84" viewBox="0 0 84 84" aria-hidden="true">
      <circle cx="46" cy="40" r="30" fill="none" stroke="var(--red)" stroke-width="5" stroke-dasharray="150 40"/>
      <text x="46" y="52" text-anchor="middle" font-family="Montserrat, sans-serif" font-weight="700" font-size="32" fill="var(--red)">24</text>
      <path d="M10 18 L22 30" stroke="var(--red)" stroke-width="7" stroke-linecap="round"/>
    </svg>
    <div class="emergency-hour">hour</div>
    <div class="emergency-note">emergency<br>service</div>
  </div>

  <h1 class="trade-title">PLUMBER,<br>DRAINER, GASFITTER/LPG</h1>
  <div class="title-rule"></div>

  <h2 class="services-heading">Our Services</h2>
  <ul class="service-list">
    <li>Blocked drains</li>
    <li>New installations</li>
    <li>Maintenance</li>
    <li>Stormwater</li>
    <li>Gutters</li>
  </ul>
  <p class="service-extra">All plumbing requirements<br>No job too small</p>
  <p class="licence">lic no 482091k.</p>

  <div class="brand">
    <div class="brand-dot"></div>
    <div class="brand-name">MOSSGATE<br>PLUMBING</div>
    <div class="brand-values">HONEST · RELIABLE · FAIR</div>
    <div class="free-quotes">FREE QUOTES</div>
  </div>

  <div class="call-box">
    <div class="call-label">CALL</div>
    <div class="call-number">0400 555 218</div>
    <div class="call-label">TODAY!</div>
  </div>

  <footer class="footer-band">
    <div>
      <svg width="16" height="20" viewBox="0 0 18 22" aria-hidden="true"><path d="M9 1a7.5 7.5 0 0 0-7.5 7.5C1.5 14 9 21 9 21s7.5-7 7.5-12.5A7.5 7.5 0 0 0 9 1z" fill="none" stroke="var(--white)" stroke-width="2"/><circle cx="9" cy="8.5" r="2.6" fill="var(--white)"/></svg>Belvine, NSW, 2590, Australia
    </div>
    <div>
      <svg width="18" height="18" viewBox="0 0 24 24" aria-hidden="true"><path d="M6.6 10.8a15 15 0 0 0 6.6 6.6l2.2-2.2c.3-.3.7-.4 1-.2 1.1.4 2.3.6 3.6.6.6 0 1 .4 1 1V20c0 .6-.4 1-1 1C10.6 21 3 13.4 3 4c0-.6.4-1 1-1h3.5c.6 0 1 .4 1 1 0 1.3.2 2.5.6 3.6.1.3 0 .7-.2 1z" fill="var(--white)"/></svg>Phone: 0400 555 218<span class="footer-gap"></span><svg width="22" height="19" viewBox="0 0 26 22" aria-hidden="true"><path d="M1 10 25 1 19 21 12 14 8 21 8 13 21 4 6 12Z" fill="var(--white)"/></svg>www.tradesbelvine.com.au
    </div>
    <div>
      Email: info@tradesbelvine.com<span class="footer-gap"></span>Facebook: MOSSGATE PLUMBING
    </div>
  </footer>
</main>
</body>
</html>
```